business card for Your Loan Scout

Please create a business card for my new business. I have attached another business card i have used previously and I like its layout and the hologram style backing with the logo. Replace the information with my new business information. On the information side of the card under the logo please place the TLCA acredited member logo I have uploaded along with 'Credit Rep Number 381749'.
next to my name in smaller text and not bold write 'JP'. and my title change from director to Broker/Director
Industry/Entity Type
Mortgage Brokerage
Contact Information for Business Card
As already on the uploaded card and in project description
Colors
Designer to choose colors to be used in the design.
Look and feel
Each slider illustrates characteristics of the customer's brand and the style your logo design should communicate.

```html
<!DOCTYPE html>
<html lang="en">
<head>
<meta charset="utf-8">
<title>Your Loan Scout – Business Card</title>
<link rel="stylesheet" href="https://fonts.googleapis.com/css2?family=Crimson+Text:wght@400;600&family=Open+Sans:wght@400&display=swap">
<style>
  :root {
    --ink: #23292a;
    --paper: #ffffff;
    --backdrop: #e6e6e6;
    --badge: #3a6fb0;
    --social: #3d4a4c;
  }
  * { margin: 0; padding: 0; box-sizing: border-box; }
  html, body { width: 1200px; height: 800px; overflow: hidden; }
  body {
    background: var(--backdrop);
    position: relative;
    font-family: "Crimson Text", Georgia, serif;
    color: var(--ink);
  }
  .card {
    position: absolute;
    left: 330px;
    width: 532px;
    height: 304px;
  }
  .card-front { top: 28px; background: var(--ink); color: var(--paper); }
  .card-back { top: 426px; background: var(--paper); overflow: hidden; }

  /* Front */
  .front-frame {
    position: absolute;
    left: 36px; top: 40px;
    width: 458px; height: 224px;
    border: 3px solid var(--paper);
  }
  .front-mark {
    position: absolute;
    left: 240px; top: 72px;
    width: 52px; height: 52px;
    border: 3px solid var(--paper);
  }
  .front-brand {
    position: absolute;
    left: 0; right: 0; top: 150px;
    text-align: center;
    font-size: 30px;
    font-weight: 600;
    letter-spacing: 0.5px;
  }
  .front-web {
    position: absolute;
    left: 0; right: 0; top: 232px;
    text-align: center;
    font-size: 15px;
  }

  /* Back – left column */
  .back-mark {
    position: absolute;
    left: 100px; top: 22px;
    width: 52px; height: 52px;
    border: 3px solid var(--ink);
  }
  .back-brand {
    position: absolute;
    left: 0; width: 252px; top: 100px;
    text-align: center;
    font-size: 29px;
    font-weight: 600;
    letter-spacing: 0.3px;
    line-height: 1.2;
  }
  .accreditation-badge {
    position: absolute;
    left: 104px; top: 150px;
    width: 44px; height: 26px;
    border-radius: 4px;
    background: var(--badge);
  }
  .credit-rep {
    position: absolute;
    left: 0; width: 252px; top: 180px;
    text-align: center;
    font-size: 13px;
    line-height: 1.2;
  }
  .find-us {
    position: absolute;
    left: 0; width: 252px; top: 208px;
    text-align: center;
    font-size: 16px;
    line-height: 1.2;
  }
  .social-links {
    position: absolute;
    left: 68px; top: 234px;
    display: flex; gap: 8px;
  }
  .social-links span {
    width: 18px; height: 18px;
    border-radius: 3px;
    background: var(--social);
  }
  .divider {
    position: absolute;
    left: 262px; top: 122px;
    width: 2px; height: 128px;
    background: var(--ink);
  }

  /* Back – right column */
  .person-name {
    position: absolute;
    left: 291px; top: 32px;
    font-size: 33px;
    font-weight: 400;
    line-height: 1;
    white-space: nowrap;
  }
  .person-name .suffix {
    font-family: "Open Sans", Arial, sans-serif;
    font-size: 14px;
    font-weight: 400;
    margin-left: 10px;
  }
  .name-rule {
    position: absolute;
    left: 291px; top: 72px;
    width: 224px; height: 2px;
    background: var(--ink);
  }
  .person-title {
    position: absolute;
    left: 291px; width: 224px; top: 76px;
    text-align: center;
    font-size: 19px;
    line-height: 1.3;
  }
  .contact-list {
    position: absolute;
    left: 280px; top: 118px;
    list-style: none;
    font-family: "Open Sans", Arial, sans-serif;
  }
  .contact-list li {
    display: flex; align-items: center;
    height: 26px; margin-bottom: 13px;
    font-size: 18px;
    white-space: nowrap;
  }
  .contact-list li.email { font-size: 15px; }
  .contact-list svg { width: 26px; height: 26px; margin-right: 12px; flex: none; }

  .footer-bar {
    position: absolute;
    top: 290px; height: 6px;
    background: var(--ink);
  }
  .footer-bar.left { left: 0; width: 189px; }
  .footer-bar.right { left: 342px; width: 190px; }
  .footer-web {
    position: absolute;
    left: 189px; width: 153px; top: 281px;
    text-align: center;
    font-size: 14px;
    line-height: 1.2;
  }
</style>
</head>
<body>

<section class="card card-front" aria-label="Card front">
  <div class="front-frame"></div>
  <div class="front-mark"></div>
  <div class="front-brand">Your Loan Scout</div>
  <div class="front-web">www.website.com</div>
</section>

<section class="card card-back" aria-label="Card back">
  <div class="back-mark"></div>
  <div class="back-brand">Your Loan Scout</div>
  <div class="accreditation-badge" role="img" aria-label="TLCA accredited member badge"></div>
  <div class="credit-rep">Credit Rep Number 381749</div>
  <div class="find-us">Find Us on:</div>
  <div class="social-links" aria-label="Social media links">
    <span></span><span></span><span></span><span></span>
  </div>
  <div class="divider"></div>

  <h1 class="person-name">Daniel Harper<span class="suffix">JP</span></h1>
  <div class="name-rule"></div>
  <div class="person-title">Broker/Director</div>

  <ul class="contact-list">
    <li>
      <svg viewBox="0 0 26 26" aria-hidden="true">
        <circle cx="13" cy="13" r="13" fill="var(--ink)"/>
        <path d="M8.5 7.5c.6-.6 1.5-.6 2 0l1.3 1.6c.4.5.4 1.2 0 1.6l-.9.9c.7 1.5 1.9 2.8 3.5 3.5l.9-.9c.4-.4 1.1-.4 1.6 0l1.6 1.3c.6.5.6 1.4 0 2l-.9.9c-.8.8-2 1-3 .6-3.2-1.3-5.700-3.8-7-7-.4-1-.2-2.200.6-3z" fill="#fff"/>
      </svg>
      0400 218 975
    </li>
    <li class="email">
      <svg viewBox="0 0 26 26" aria-hidden="true">
        <circle cx="13" cy="13" r="13" fill="var(--ink)"/>
        <rect x="7" y="9" width="12" height="8.5" fill="none" stroke="#fff" stroke-width="1.3"/>
        <path d="M7 9l6 5 6-5" fill="none" stroke="#fff" stroke-width="1.3"/>
      </svg>
      dan@harpergroup.au
    </li>
    <li>
      <svg viewBox="0 0 26 26" aria-hidden="true">
        <circle cx="13" cy="13" r="13" fill="var(--ink)"/>
        <path d="M13 6.5a4.5 4.5 0 0 0-4.5 4.5c0 3.2 4.5 8.5 4.5 8.5s4.5-5.3 4.5-8.5A4.5 4.5 0 0 0 13 6.5z" fill="#fff"/>
        <circle cx="13" cy="11" r="1.6" fill="var(--ink)"/>
      </svg>
      harpergroup.au
    </li>
  </ul>

  <div class="footer-bar left"></div>
  <div class="footer-web">www.website.com</div>
  <div class="footer-bar right"></div>
</section>

</body>
</html>
```